Webdesign für Brenner Flusstrom
Zielgruppe
Ansprechpartner für Planung und Errichtung von Stromerzeugung durch erneuerbare Energien. Alle Interessen im privaten, teilöffentlichen und öffentlichen Bereich, die mittel- und langfristig umweltschonenden Strom nutzen wollen.
Aufgabenstellung
- Farben bitte in den Unternehmensfarben Blau/Weiß mit einem kleinen Anteil Orange
- Bilder nach Möglichkeit bitte nur eigene (siehe Anhang)
- klare und übersichtliche Struktur
- KEIN Abklatsch der alten Webseite

```html
<!DOCTYPE html>
<html lang="de">
<head>
<meta charset="utf-8">
<title>Brenner Flusstrom – Erneuerbare Energien</title>
<link href="https://fonts.googleapis.com/css2?family=Poppins:wght@500;600;700&family=Roboto:wght@700&family=Roboto+Condensed:wght@400&display=swap" rel="stylesheet">
<style>
  :root {
    --navy: #0e0b86;
    --navy-deep: #1a1f8e;
    --white: #ffffff;
    --topbar-bg: #f2f2f4;
    --rule: #1b1b8a;
    --text-muted: #333344;
  }
  * { margin: 0; padding: 0; box-sizing: border-box; }
  html, body { width: 1200px; height: 579px; overflow: hidden; background: var(--white); }
  body { position: relative; font-family: "Poppins", sans-serif; color: var(--navy); }

  .topbar {
    position: absolute; top: 0; left: 0; width: 1200px; height: 26px;
    background: var(--topbar-bg); border-bottom: 1px solid var(--rule);
  }
  .topbar-mail { position: absolute; left: 222px; top: 7px; display: flex; align-items: center; gap: 17px; font-size: 9px; font-weight: 500; }
  .topbar-claim { position: absolute; left: 0; width: 1189px; top: 9px; text-align: center; font-size: 9.5px; font-weight: 500; letter-spacing: 0.1px; }
  .topbar-address { position: absolute; left: 821px; top: 3px; display: flex; align-items: center; gap: 12px; }
  .address-lines { line-height: 1.1; }
  .address-street { font-size: 9.5px; font-weight: 500; }
  .address-city { font-family: "Roboto Condensed", sans-serif; font-size: 8.5px; }

  .navbar { position: absolute; top: 27px; left: 0; width: 1200px; height: 52px; background: var(--white); }
  .nav-brand { position: absolute; left: 230px; top: 17px; display: flex; align-items: center; gap: 4px; font-size: 9px; font-weight: 700; }
  .nav-brand .dot { width: 10px; height: 10px; border-radius: 50%; background: var(--navy); }
  .nav-menu { position: absolute; left: 469px; top: 18px; display: flex; gap: 14px; font-size: 11.5px; font-weight: 700; list-style: none; }
  .nav-menu li { display: flex; align-items: center; gap: 4px; }

  .hero {
    position: absolute; top: 79px; left: 0; width: 1189px; height: 375px;
    background: linear-gradient(180deg, #26248f 0%, #3a4aa8 35%, #3f5fb8 65%, #2a4aa2 100%);
  }
  .hero-brand { position: absolute; top: 109px; left: 0; width: 1189px; display: flex; justify-content: center; align-items: center; gap: 10px; color: var(--white); font-size: 22px; font-weight: 700; }
  .hero-brand .dot { width: 26px; height: 26px; border-radius: 50%; background: var(--white); }
  .hero-title { position: absolute; top: 189px; left: 0; width: 1189px; text-align: center; font-family: "Roboto", sans-serif; font-weight: 700; font-size: 25px; color: var(--white); }

  .services { position: absolute; top: 381px; left: 0; width: 1189px; }
  .service { position: absolute; width: 220px; text-align: center; }
  .service-photo { width: 150px; height: 150px; border-radius: 50%; margin: 0 auto; }
  .service-title { margin-top: 19px; font-size: 12.5px; font-weight: 700; letter-spacing: 0.2px; }
  .service-text { margin-top: 7px; font-size: 8px; color: var(--text-muted); }
  .photo-water { background: radial-gradient(circle at 50% 40%, #6c95a8, #2f6a6a 55%, #123c44); }
  .photo-solar { background: linear-gradient(180deg, #4fa6e8 0%, #9fcbe8 35%, #3b5db0 55%, #4f8a34 85%); }
  .photo-emob { background: radial-gradient(circle at 60% 40%, #b7895a, #2a46b0 50%, #101a5a); }
</style>
</head>
<body>
  <header class="topbar">
    <div class="topbar-mail">
      <svg width="13" height="10" viewBox="0 0 13 10"><rect width="13" height="10" rx="1.5" fill="var(--navy)"/><path d="M1 1.5 L6.5 5.5 L12 1.5" stroke="#fff" stroke-width="1.3" fill="none"/></svg>
      <span>info@brenner-flusstrom.de</span>
    </div>
    <div class="topbar-claim">IHR PROFI FÜR ERNEUERBARE ENERGIEN</div>
    <div class="topbar-address">
      <svg width="11" height="15" viewBox="0 0 11 15"><path d="M5.5 0 C2.5 0 0 2.4 0 5.4 C0 9.4 5.5 15 5.5 15 C5.5 15 11 9.4 11 5.4 C11 2.4 8.5 0 5.5 0 Z" fill="var(--navy)"/><circle cx="5.5" cy="5.3" r="2" fill="#f2f2f4"/></svg>
      <div class="address-lines">
        <div class="address-street">Birkenweg 18</div>
        <div class="address-city">09111 Talheim</div>
      </div>
    </div>
  </header>

  <nav class="navbar">
    <div class="nav-brand"><span class="dot"></span>Brenner Flusstrom</div>
    <ul class="nav-menu">
      <li>Über Uns</li>
      <li>Leistungen <svg width="7" height="5" viewBox="0 0 7 5"><path d="M1 1 L3.5 3.5 L6 1" stroke="var(--navy)" stroke-width="1.3" fill="none"/></svg></li>
      <li>Karriere</li>
      <li>Kontakt</li>
    </ul>
  </nav>

  <section class="hero" role="img" aria-label="Foto: schwimmende Solarmodule auf einem See unter blauem Himmel">
    <div class="hero-brand"><span class="dot"></span>Brenner Flusstrom</div>
    <h1 class="hero-title">IHR PARTNER FÜR ERNEUERBARE ENERGIEN</h1>
  </section>

  <section class="services">
    <article class="service" style="left:253px">
      <div class="service-photo photo-water" role="img" aria-label="Foto: Staudamm eines Wasserkraftwerks in einer Seenlandschaft"></div>
      <h2 class="service-title">WASSERKRAFT</h2>
      <p class="service-text">Nutzen Sie die Kraft des Wassers</p>
    </article>
    <article class="service" style="left:484px">
      <div class="service-photo photo-solar" role="img" aria-label="Foto: Solarmodule auf einer Blumenwiese unter blauem Himmel"></div>
      <h2 class="service-title">PHOTOVOLTAIK</h2>
      <p class="service-text">Wir holen Sonnenlicht in Ihr Stromnetz</p>
    </article>
    <article class="service" style="left:716px">
      <div class="service-photo photo-emob" role="img" aria-label="Foto: Elektroauto an einer Ladestation"></div>
      <h2 class="service-title">ELEKTROMOBILITÄT</h2>
      <p class="service-text">Fahren Sie mit Strom aus eigener Quelle</p>
    </article>
  </section>
</body>
</html>
```